It's a new electrical company based in Newcastle NSW. I would like a logo between the two words "BRYN (insert logo) VOLT". I would like the logo to represent electrical and celtic style. For example I have seen a light bulb with a celtic pattern in the middle which looked very good. I would like it to be a white card, mainly black writing and quite basic not too much going on. But maybe have the logo partially red or green?

BRYN VOLT
Electrical Contractors
Domestic, commercial, fault finding, testing, re wires, switchboard upgrades
License No: 738421K
Fully Insured
Phone: 0431587720

```html
<!DOCTYPE html>
<html lang="en">
<head>
<meta charset="utf-8">
<title>Bryn Volt – Business Card</title>
<link href="https://fonts.googleapis.com/css2?family=Open+Sans:wght@400;600;700&display=swap" rel="stylesheet">
<style>
  :root {
    --page-bg: #e4e4e2;
    --card-white: #f7f7f6;
    --ink: #2b2b2b;
    --band-black: #141414;
    --band-text: #f2f2f2;
    --accent-green: #1a9a3c;
  }
  html, body {
    margin: 0;
    padding: 0;
    width: 1200px;
    height: 1000px;
    overflow: hidden;
    background: var(--page-bg);
    font-family: "Open Sans", Arial, sans-serif;
  }
  .business-card {
    position: absolute;
    left: 150px;
    top: 243px;
    width: 900px;
    height: 514px;
    background: var(--card-white);
    box-shadow: 0 10px 30px rgba(0,0,0,0.18);
    overflow: hidden;
  }
  .card-phone {
    position: absolute;
    top: 34px;
    right: 46px;
    margin: 0;
    font-size: 21px;
    font-weight: 600;
    color: var(--ink);
    letter-spacing: 0.3px;
  }
  .brand {
    position: absolute;
    left: 0;
    right: 0;
    top: 140px;
    display: flex;
    flex-direction: column;
    align-items: center;
  }
  .brand-lockup {
    display: flex;
    align-items: center;
    gap: 26px;
  }
  .brand-word {
    font-size: 86px;
    font-weight: 700;
    line-height: 1;
    color: var(--ink);
    letter-spacing: -1px;
  }
  .brand-dot {
    width: 64px;
    height: 64px;
    border-radius: 50%;
    background: var(--accent-green);
    flex: none;
  }
  .brand-tagline {
    margin: 10px 0 0 60px;
    font-size: 29px;
    font-weight: 400;
    color: var(--ink);
  }
  .services-band {
    position: absolute;
    left: 0;
    right: 0;
    bottom: 0;
    height: 124px;
    background: var(--band-black);
    color: var(--band-text);
    display: flex;
    flex-direction: column;
    justify-content: center;
    align-items: center;
    gap: 6px;
    font-size: 19px;
    font-weight: 400;
    letter-spacing: 0.2px;
  }
  .services-band p { margin: 0; }
</style>
</head>
<body>
  <article class="business-card">
    <p class="card-phone">Tel: 0431587720</p>

    <div class="brand">
      <div class="brand-lockup" aria-label="BRYN VOLT">
        <span class="brand-word">BRYN</span>
        <span class="brand-dot" aria-hidden="true"></span>
        <span class="brand-word">VOLT</span>
      </div>
      <p class="brand-tagline">Electrical Contractors</p>
    </div>

    <footer class="services-band">
      <p class="services-list">Domestic, Commercial, Fault Finding, Testing, Re-wires, Switchboard Upgrades</p>
      <p class="license-line">License No: 738421K . Fully Insured</p>
    </footer>
  </article>
</body>
</html>
```